KiteSurf Weather App Forecast Screen re-design (1 Screen)

We are redesigning our application, BreezeLoom. Our main screen is the forecast screen. The forecast screen presents the forecast for multiple places for the selected day.

Intro
-----

The user has a list of favorite spots that he is monitoring. Then he selects the date that he wants to get the forecast. The forecast screen presents a list of all the spots and a summary of the weather conditions. Spots are sorted by weather conditions. At the top, he gets the spot with the best weather conditions. We have an algorithm that can evaluate whether given weather conditions are good or not. When they are good we indicate that to the user.

Current Solution
------------------

There is also a landscape version, which contains a bit more data: "Current Forecast Screen Lanscape.jpeg". The landscape one is a bit funny, as it is taken from an Zentra Q and the app was not designed for it at the time.

The bars that you see for each hour use our algorithm to display whether the conditions are good:

- When the color is gray the conditions are not good
- When the color is yellow there are light wind conditions
- When the color is green there are good
- When the color is red the wind is very strong
- The height of the bar indicates wind strength

More Info
-----------

The detailed forecast screen is also attached so you can get a bit more context, "DetailedForecast.jpeg"

An example from an application that has a similar chart is attached, "SimilarApp.jpeg". I have circled the chart with red.

Future Solution
------------------

(See note.jpeg)

We want to create a page that contains more information and passes a better message to our users.

The elements that are important and we want to present to the user are the following:

1. Wind. (The most important)
It contains two elements: strength and direction.

1.1 Wind Strength.
Good wind strength is anything between 10-45 knots (measurement unit like km/h). The best representation with a color palette.
Gray will be the color used when the strength is not between 10-45.
The palette should start with yellow at 10 knots, then move toward green for 22knots and finally go towards red for 45 knots.

1.2 Wind Direction.
There are good wind directions that we can kite and directions that is is not possible.
Can be presented by an arrow that points in the direction the wind is blowing to. The color of the arrow will be green when the direction is good, yellow when it is average and gray when it is not good.

My thought for portrait mode is to use an arrow point for the direction and the color of the arrow to represent the strength. Solution number 2 on my notes. Then for landscape, we could use both a number and an arrow like number 4 on my notes.

2. Wave.
It contains three elements: height, period and direction. It is not displayed to all of our users only the ones that have selected the wave riding option.

2.1 Height is represented by a number. Ex. 1.2 meters or 2 foot.
2.2 Period is represented in seconds. Ex. 12 seconds.
2.3 Directions is an arrow that points to the direction the wave is coming from.

Again the solution should be like the wind. Arrow for direction and the color of the arrow for height. The palette here should be something with different blue colors.

3. Tide height. (Optional for tidal spots, as not all spots have tides)

The best way to represent that it through a graph. I would also like to see an alternative, where we have three symbols for low, mid and high tide.

4. General Weather. Rain/Snow and temperature.

This should be represented by a sun/cloud/rain symbol. If it is very cold the symbol can also contain an ice sign on the background.

---------

This is a guideline creativity will be valued. Maybe there is another way to do it that I have not thought about.

The winner of the competition will have to send us all graphics used in vector format, so we can input them to our xCode project.

Finally the person that wins the competition will be the first one to be considered for the redesign of the rest of our application.

Target Market(s)

Kitesurfers

Font styles to use
Sans Serif

Colors

Designer to choose colors to be used in the design.

Requirements
Must have
• It should be minimal and clearly communicate the weather forecast to my users. It should be user friendly.
Nice to have
• Communicative color palettes for both wind strength, tide and waves
Should not have
• Hard to understand UI

```html
<!DOCTYPE html>
<html lang="en">
<head>
<meta charset="utf-8">
<title>BreezeLoom – Forecast</title>
<link href="https://fonts.googleapis.com/css2?family=Roboto:wght@300;400;700&display=swap" rel="stylesheet">
<style>
  :root {
    --page-bg: #eef2f7;
    --white: #ffffff;
    --navy: #1d3a7a;
    --accent-blue: #2f7fe0;
    --header-blue: #3a90e4;
    --header-grey: #858585;
    --soft-blue: #7fb4ea;
    --wave-blue: #5fa0ea;
    --column-shade: #eaf3fd;
    --divider: #e6edf5;
    --sun-yellow: #f8d21e;
    --wind-green: #6bb81f;
    --wind-grey: #b8b8b8;
    --wind-red: #d8304a;
    --wind-yellow: #f5c800;
    --tide-high: #1d3f8f;
    --tide-mid: #8dc0f0;
    --tide-low: #c2c2c2;
  }
  * { box-sizing: border-box; margin: 0; padding: 0; }
  html, body { width: 674px; height: 1200px; overflow: hidden; }
  body {
    background: var(--page-bg);
    font-family: "Roboto", sans-serif;
    position: relative;
  }
  .date-bar {
    position: absolute; left: 0; top: 0; width: 674px; height: 84px;
    background: var(--white);
    box-shadow: 0 2px 6px rgba(30, 60, 110, .08);
  }
  .date-bar .today { position: absolute; left: 42px; top: 29px; width: 32px; height: 32px; }
  .date-bar .nav { position: absolute; top: 31px; width: 14px; height: 28px; }
  .date-bar .prev { left: 91px; }
  .date-bar .next { left: 633px; }
  .date-bar .day {
    position: absolute; top: 27px; width: 50px; margin-left: -25px;
    text-align: center; font-size: 25px; font-weight: 400; color: var(--navy);
  }
  .spot-card {
    position: absolute; left: 27px; width: 621px; height: 490px;
    background: var(--white); border-radius: 32px; overflow: hidden;
    box-shadow: 0 4px 14px rgba(30, 60, 110, .08);
  }
  .spot-card.cape { top: 108px; }
  .spot-card.bigbay { top: 630px; }
  .spot-header {
    height: 94px; position: relative; color: var(--white);
  }
  .cape .spot-header { background: var(--header-blue); }
  .bigbay .spot-header { background: var(--header-grey); }
  .spot-name {
    position: absolute; left: 31px; top: 28px; font-size: 33px; font-weight: 700; letter-spacing: -.3px;
  }
  .spot-icon { position: absolute; left: 405px; top: 16px; width: 66px; height: 66px; }
  .spot-temp { position: absolute; right: 30px; top: 30px; white-space: nowrap; }
  .spot-temp .low { font-size: 27px; font-weight: 300; color: #a9d0f7; }
  .bigbay .spot-temp .low { color: #a9d0f7; }
  .spot-temp .high { font-size: 33px; font-weight: 400; color: var(--white); }
  .forecast-table { margin-left: 33px; width: 562px; }
  .row { display: flex; height: 100px; border-bottom: 1px solid var(--divider); }
  .row.tide { height: 96px; border-bottom: 0; position: relative; }
  .label { width: 58px; display: flex; align-items: center; justify-content: center; }
  .label svg { width: 40px; height: 40px; }
  .cell {
    width: 72px; display: flex; flex-direction: column; align-items: center;
    position: relative;
  }
  .cell.shade { background: var(--column-shade); }
  .weather .cell { padding-top: 20px; }
  .weather .cell svg { width: 28px; height: 28px; }
  .weather .value { margin-top: 6px; font-size: 19px; font-weight: 300; color: var(--soft-blue); }
  .wind .cell { padding-top: 20px; }
  .wind .cell svg { width: 26px; height: 26px; }
  .wind .value { margin-top: 6px; font-size: 20px; font-weight: 400; }
  .green { color: var(--wind-green); }
  .grey { color: var(--wind-grey); }
  .red { color: var(--wind-red); }
  .yellow { color: var(--wind-yellow); }
  .wave .cell { padding-top: 13px; color: var(--wave-blue); }
  .wave .cell svg { width: 26px; height: 26px; }
  .wave .value { font-size: 19px; font-weight: 300; color: var(--soft-blue); line-height: 24px; }
  .wave .value:first-of-type { margin-top: 3px; }
  .tide-line {
    position: absolute; left: 58px; right: 0; height: 0;
    border-top: 1px dashed #d7e2ee;
  }
  .tide-line.high { top: 26px; }
  .tide-line.mid { top: 48px; }
  .tide-line.low { top: 69px; }
  .dot { position: absolute; left: 31px; width: 10px; height: 10px; border-radius: 50%; }
  .dot.high { top: 21px; background: var(--tide-high); }
  .dot.mid { top: 43px; background: var(--tide-mid); }
  .dot.low { top: 64px; background: var(--tide-low); }
</style>
</head>
<body>

<svg width="0" height="0" style="position:absolute">
  <defs>
    <symbol id="sun" viewBox="0 0 24 24">
      <g fill="none" stroke="currentColor" stroke-width="1.6" stroke-linecap="round">
        <circle cx="12" cy="12" r="5"/>
        <path d="M12 2v2.5M12 19.5V22M2 12h2.5M19.5 12H22M4.9 4.9l1.8 1.8M17.3 17.3l1.8 1.8M4.9 19.1l1.8-1.8M17.3 6.7l1.8-1.8"/>
      </g>
    </symbol>
    <symbol id="cloud-sun" viewBox="0 0 24 24">
      <g fill="none" stroke="currentColor" stroke-width="1.6" stroke-linecap="round">
        <path d="M12.5 8.2a4 4 0 0 1 7 3.3"/>
        <path d="M16 2v2M21.8 5.2l-1.4 1.4M23 11h-1.5M10.2 5.2l1.4 1.4"/>
        <path d="M5.5 20h11a3.2 3.2 0 0 0 .2-6.4 4.8 4.8 0 0 0-9.2-.9A3.7 3.7 0 0 0 5.5 20z"/>
      </g>
    </symbol>
    <symbol id="arrow" viewBox="0 0 24 24">
      <path d="M4 3 L22 12 L4 21 L9.5 12 Z" fill="currentColor"/>
    </symbol>
  </defs>
</svg>

<header class="date-bar">
  <svg class="today" viewBox="0 0 32 32" fill="none" stroke="#1d3a7a" stroke-width="2" stroke-linecap="round" stroke-linejoin="round">
    <circle cx="16" cy="16" r="14"/><path d="M10 16.5l4 4 8-9"/>
  </svg>
  <svg class="nav prev" viewBox="0 0 14 28" fill="none" stroke="#cfd8e4" stroke-width="2" stroke-linecap="round"><path d="M11 3 L3 14 L11 25"/></svg>
  <span class="day" style="left:157px">08</span>
  <span class="day" style="left:229px">09</span>
  <span class="day" style="left:296px">10</span>
  <span class="day" style="left:369px">11</span>
  <span class="day" style="left:445px">12</span>
  <span class="day" style="left:514px">13</span>
  <span class="day" style="left:584px">14</span>
  <svg class="nav next" viewBox="0 0 14 28" fill="none" stroke="#cfd8e4" stroke-width="2" stroke-linecap="round"><path d="M3 3 L11 14 L3 25"/></svg>
</header>

<!-- Spot: Cape town -->
<section class="spot-card cape">
  <div class="spot-header">
    <h2 class="spot-name">Cape town</h2>
    <svg class="spot-icon" style="color:var(--sun-yellow)" viewBox="0 0 24 24"><g fill="none" stroke="currentColor" stroke-width="1.5" stroke-linecap="round"><circle cx="12" cy="12" r="5.5"/><path d="M12 1.5v2.5M12 20v2.5M1.5 12H4M20 12h2.5M4.6 4.6l1.7 1.7M17.7 17.7l1.7 1.7M4.6 19.4l1.7-1.7M17.7 6.3l1.7-1.7"/></g></svg>
    <div class="spot-temp"><span class="low">10°</span> <span class="high">15°</span></div>
  </div>
  <div class="forecast-table">
    <div class="row weather">
      <div class="label"><svg viewBox="0 0 40 40" fill="none" stroke="#2f7fe0" stroke-width="2.2"><path d="M16 6a4 4 0 0 1 8 0v18a7 7 0 1 1-8 0z"/><circle cx="20" cy="30" r="3" fill="#2f7fe0"/><path d="M20 14v13"/></svg></div>
      <div class="cell shade" style="color:var(--soft-blue)"><svg><use href="#cloud-sun"/></svg><span class="value">8ºC</span></div>
      <div class="cell" style="color:var(--soft-blue)"><svg><use href="#cloud-sun"/></svg><span class="value">8ºC</span></div>
      <div class="cell shade" style="color:var(--soft-blue)"><svg><use href="#sun"/></svg><span class="value">9ºC</span></div>
      <div class="cell" style="color:var(--soft-blue)"><svg><use href="#sun"/></svg><span class="value">10ºC</span></div>
      <div class="cell shade" style="color:var(--soft-blue)"><svg><use href="#sun"/></svg><span class="value">12ºC</span></div>
      <div class="cell" style="color:var(--soft-blue)"><svg><use href="#sun"/></svg><span class="value">14ºC</span></div>
      <div class="cell shade" style="color:var(--soft-blue)"><svg><use href="#sun"/></svg><span class="value">15ºC</span></div>
    </div>
    <div class="row wind">
      <div class="label"><svg viewBox="0 0 40 40" fill="none" stroke="#2f7fe0" stroke-width="2.2" stroke-linecap="round"><path d="M6 15h18a4 4 0 1 0-4-4"/><path d="M4 21h24a5 5 0 1 1-5 5"/><path d="M9 27h8"/></svg></div>
      <div class="cell shade green"><svg><use href="#arrow"/></svg><span class="value">22kn</span></div>
      <div class="cell grey"><svg style="transform:rotate(-60deg)"><use href="#arrow"/></svg><span class="value">6kn</span></div>
      <div class="cell shade red"><svg style="transform:rotate(90deg)"><use href="#arrow"/></svg><span class="value">45kn</span></div>
      <div class="cell grey"><svg style="transform:rotate(135deg)"><use href="#arrow"/></svg><span class="value">2kn</span></div>
      <div class="cell shade yellow"><svg style="transform:rotate(45deg)"><use href="#arrow"/></svg><span class="value">17kn</span></div>
      <div class="cell grey"><svg style="transform:rotate(-60deg)"><use href="#arrow"/></svg><span class="value">8kn</span></div>
      <div class="cell shade green"><svg><use href="#arrow"/></svg><span class="value">28kn</span></div>
    </div>
    <div class="row wave">
      <div class="label"><svg viewBox="0 0 40 40" fill="none" stroke="#2f7fe0" stroke-width="2.4" stroke-linecap="round"><path d="M3 26c4 0 5-8 10-8s4 6 7 6 3-6 7-6 4 6 7 6 3-3 4-4"/><path d="M11 26c2-1 3-4 6-4"/></svg></div>
      <div class="cell shade"><svg><use href="#arrow"/></svg><span class="value">1.2</span><span class="value">12s</span></div>
      <div class="cell"><svg style="transform:rotate(-60deg)"><use href="#arrow"/></svg><span class="value">2.2</span><span class="value">15s</span></div>
      <div class="cell shade"><svg style="transform:rotate(180deg)"><use href="#arrow"/></svg><span class="value">1.4</span><span class="value">26s</span></div>
      <div class="cell"><svg style="transform:rotate(-60deg)"><use href="#arrow"/></svg><span class="value">4.1</span><span class="value">18s</span></div>
      <div class="cell shade"><svg style="transform:rotate(-60deg)"><use href="#arrow"/></svg><span class="value">1.1</span><span class="value">34s</span></div>
      <div class="cell"><svg style="transform:rotate(180deg)"><use href="#arrow"/></svg><span class="value">1.4</span><span class="value">26s</span></div>
      <div class="cell shade"><svg style="transform:rotate(-60deg)"><use href="#arrow"/></svg><span class="value">2.2</span><span class="value">15s</span></div>
    </div>
    <div class="row tide">
      <div class="label"><svg viewBox="0 0 40 40" fill="none" stroke="#2f7fe0" stroke-width="2.2" stroke-linecap="round"><path d="M20 5v12M15 10l5-5 5 5"/><path d="M4 24c3 0 3-2 6-2s3 2 6 2 3-2 6-2 3 2 6 2 3-2 6-2"/><path d="M4 30c3 0 3-2 6-2s3 2 6 2 3-2 6-2 3 2 6 2 3-2 6-2"/></svg></div>
      <div class="cell shade"><span class="dot mid"></span></div>
      <div class="cell"><span class="dot high"></span></div>
      <div class="cell shade"><span class="dot mid"></span></div>
      <div class="cell"><span class="dot low"></span></div>
      <div class="cell shade"><span class="dot mid"></span></div>
      <div class="cell"><span class="dot low"></span></div>
      <div class="cell shade"><span class="dot high"></span></div>
      <span class="tide-line high"></span><span class="tide-line mid"></span><span class="tide-line low"></span>
    </div>
  </div>
</section>

<!-- Spot: Big bay -->
<section class="spot-card bigbay">
  <div class="spot-header">
    <h2 class="spot-name">Big bay</h2>
    <svg class="spot-icon" style="color:#c4c4c4" viewBox="0 0 24 24"><g fill="none" stroke="currentColor" stroke-width="1.4" stroke-linecap="round"><path d="M12.5 8.2a4 4 0 0 1 7 3.3"/><path d="M16 2v2M21.8 5.2l-1.4 1.4M23 11h-1.5M10.2 5.2l1.4 1.4"/><path d="M4.5 18.5h11a3.2 3.2 0 0 0 .2-6.4 4.8 4.8 0 0 0-9.2-.9A3.7 3.7 0 0 0 4.5 18.5z"/><path d="M6 21.5l.6-1M9 21.5l.6-1M12 21.5l.6-1"/></g></svg>
    <div class="spot-temp"><span class="low">10°</span> <span class="high">15°</span></div>
  </div>
  <div class="forecast-table">
    <div class="row weather">
      <div class="label"><svg viewBox="0 0 40 40" fill="none" stroke="#2f7fe0" stroke-width="2.2"><path d="M16 6a4 4 0 0 1 8 0v18a7 7 0 1 1-8 0z"/><circle cx="20" cy="30" r="3" fill="#2f7fe0"/><path d="M20 14v13"/></svg></div>
      <div class="cell shade" style="color:var(--soft-blue)"><svg><use href="#cloud-sun"/></svg><span class="value">8ºC</span></div>
      <div class="cell" style="color:var(--soft-blue)"><svg><use href="#cloud-sun"/></svg><span class="value">8ºC</span></div>
      <div class="cell shade" style="color:var(--soft-blue)"><svg><use href="#sun"/></svg><span class="value">9ºC</span></div>
      <div class="cell" style="color:var(--soft-blue)"><svg><use href="#sun"/></svg><span class="value">10ºC</span></div>
      <div class="cell shade" style="color:var(--soft-blue)"><svg><use href="#sun"/></svg><span class="value">12ºC</span></div>
      <div class="cell" style="color:var(--soft-blue)"><svg><use href="#sun"/></svg><span class="value">14ºC</span></div>
      <div class="cell shade" style="color:var(--soft-blue)"><svg><use href="#sun"/></svg><span class="value">15ºC</span></div>
    </div>
    <div class="row wind">
      <div class="label"><svg viewBox="0 0 40 40" fill="none" stroke="#2f7fe0" stroke-width="2.2" stroke-linecap="round"><path d="M6 15h18a4 4 0 1 0-4-4"/><path d="M4 21h24a5 5 0 1 1-5 5"/><path d="M9 27h8"/></svg></div>
      <div class="cell shade green"><svg><use href="#arrow"/></svg><span class="value">22kn</span></div>
      <div class="cell grey"><svg style="transform:rotate(-60deg)"><use href="#arrow"/></svg><span class="value">6kn</span></div>
      <div class="cell shade red"><svg style="transform:rotate(90deg)"><use href="#arrow"/></svg><span class="value">45kn</span></div>
      <div class="cell grey"><svg style="transform:rotate(135deg)"><use href="#arrow"/></svg><span class="value">2kn</span></div>
      <div class="cell shade yellow"><svg style="transform:rotate(45deg)"><use href="#arrow"/></svg><span class="value">17kn</span></div>
      <div class="cell grey"><svg style="transform:rotate(-60deg)"><use href="#arrow"/></svg><span class="value">8kn</span></div>
      <div class="cell shade green"><svg><use href="#arrow"/></svg><span class="value">28kn</span></div>
    </div>
    <div class="row wave">
      <div class="label"><svg viewBox="0 0 40 40" fill="none" stroke="#2f7fe0" stroke-width="2.4" stroke-linecap="round"><path d="M3 26c4 0 5-8 10-8s4 6 7 6 3-6 7-6 4 6 7 6 3-3 4-4"/><path d="M11 26c2-1 3-4 6-4"/></svg></div>
      <div class="cell shade"><svg><use href="#arrow"/></svg><span class="value">1.2</span><span class="value">12s</span></div>
      <div class="cell"><svg style="transform:rotate(-60deg)"><use href="#arrow"/></svg><span class="value">2.2</span><span class="value">15s</span></div>
      <div class="cell shade"><svg style="transform:rotate(180deg)"><use href="#arrow"/></svg><span class="value">1.4</span><span class="value">26s</span></div>
      <div class="cell"><svg style="transform:rotate(-60deg)"><use href="#arrow"/></svg><span class="value">4.1</span><span class="value">18s</span></div>
      <div class="cell shade"><svg style="transform:rotate(-60deg)"><use href="#arrow"/></svg><span class="value">1.1</span><span class="value">34s</span></div>
      <div class="cell"><svg style="transform:rotate(180deg)"><use href="#arrow"/></svg><span class="value">1.4</span><span class="value">26s</span></div>
      <div class="cell shade"><svg style="transform:rotate(-60deg)"><use href="#arrow"/></svg><span class="value">2.2</span><span class="value">15s</span></div>
    </div>
    <div class="row tide">
      <div class="label"><svg viewBox="0 0 40 40" fill="none" stroke="#2f7fe0" stroke-width="2.2" stroke-linecap="round"><path d="M20 5v12M15 10l5-5 5 5"/><path d="M4 24c3 0 3-2 6-2s3 2 6 2 3-2 6-2 3 2 6 2 3-2 6-2"/><path d="M4 30c3 0 3-2 6-2s3 2 6 2 3-2 6-2 3 2 6 2 3-2 6-2"/></svg></div>
      <div class="cell shade"><span class="dot mid"></span></div>
      <div class="cell"><span class="dot high"></span></div>
      <div class="cell shade"><span class="dot mid"></span></div>
      <div class="cell"><span class="dot low"></span></div>
      <div class="cell shade"><span class="dot mid"></span></div>
      <div class="cell"><span class="dot low"></span></div>
      <div class="cell shade"><span class="dot high"></span></div>
      <span class="tide-line high"></span><span class="tide-line mid"></span><span class="tide-line low"></span>
    </div>
  </div>
</section>

</body>
</html>
```